I need a direct mail postcard made up for my marketing campaign

I am starting a marketing campaign and need a design for a post card. I own an iron door company and need to have before and after images on the post card to showcase what our work looks like. I have provided pictures to use below.

The design needs to be two sided. The logo should be on the front.

The tag line for this campaign is: Design the smile your home deserves.

Words to also use: Distinctive style, Work of Art, One-of-a-Kind, Elegant, Modern, Innovative, Unique

My information for the card
Name: Dean Harlowe
Phone number: (555)-318-2764
Email: Dean@wroughtgatestudio.example

The US postal system is very picky as to what can be sent in the mail. The only requirement they have is for the address. There needs to be a 2inch (50.8mm) by 4inch (101.6mm) blank space on the bottom right hand corner on the back of the card.

Target Market(s)

Home owners

Industry/Entity Type

Home Improvement

Font styles to use
Serif
Decorative

Colors
0555a3
ffffff
ec1f27

Requirements
Must have
• My logo, My contact information, before and after pictures
• Provided 3D images
Nice to have
• Words that describe iron doors
• A contrast between contemporary and ornate doors.

```html
<!DOCTYPE html>
<html lang="en">
<head>
<meta charset="utf-8">
<title>Wrought Gate Studio – Direct Mail Postcard</title>
<link rel="stylesheet" href="https://fonts.googleapis.com/css2?family=Barlow+Semi+Condensed:wght@400;600;700&family=Nunito+Sans:wght@400;600&display=swap">
<style>
  :root {
    --brand-blue: #0555a3;
    --brand-red: #ec1f27;
    --paper: #ffffff;
    --canvas: #ffffff;
    --photo-portrait: linear-gradient(160deg, #9aa3ad 0%, #3b3f47 60%, #1d2026 100%);
    --photo-modern: linear-gradient(180deg, #f1f0ee 0%, #dcd8d2 100%);
    --photo-before: linear-gradient(180deg, #7a3a22 0%, #5a2a18 100%);
    --photo-after: linear-gradient(180deg, #3a3330 0%, #8a6a3a 45%, #2a2422 100%);
    --font-display: "Barlow Semi Condensed", "Arial Narrow", sans-serif;
    --font-body: "Nunito Sans", Arial, sans-serif;
  }
  * { box-sizing: border-box; margin: 0; padding: 0; }
  html, body { width: 1200px; height: 1000px; overflow: hidden; background: var(--canvas); }
  .stage { position: relative; width: 1200px; height: 1000px; }

  .postcard {
    position: absolute; width: 621px; height: 403px;
    background: var(--paper); overflow: hidden;
    box-shadow: 0 1px 5px rgba(0,0,0,.28);
  }
  .postcard--back { left: 128px; top: 104px; }
  .postcard--front { left: 476px; top: 465px; }
  .postcard svg { position: absolute; inset: 0; }

  .shape-blue { fill: var(--brand-blue); }
  .shape-red { fill: var(--brand-red); }

  .cta-heading { font-family: var(--font-display); font-weight: 700; font-size: 27px; fill: var(--paper); }
  .cta-phone { font-family: var(--font-body); font-weight: 400; font-size: 30px; fill: var(--paper); }
  .cta-email { font-family: var(--font-body); font-weight: 400; font-size: 15px; fill: var(--paper); }

  .tagline { font-family: var(--font-display); font-weight: 700; font-size: 29px; fill: var(--brand-blue); }
  .brand-name { font-family: var(--font-display); font-weight: 700; font-size: 8px; fill: var(--brand-blue); letter-spacing: .5px; }
  .subline { font-family: var(--font-body); font-size: 10.5px; fill: var(--paper); letter-spacing: 2.2px; }
  .photo-label { font-family: var(--font-body); font-size: 10.5px; fill: var(--paper); }
  .owner-name { font-family: var(--font-body); font-size: 11px; fill: var(--paper); letter-spacing: .3px; }
  .contact-line { font-family: var(--font-body); font-weight: 600; font-size: 16px; fill: var(--paper); }

  .photo { position: absolute; }
  .photo--portrait { left: 0; top: 103px; width: 128px; height: 219px; background: var(--photo-portrait); }
  .photo--modern { left: 209px; top: 103px; width: 155px; height: 219px; background: var(--photo-modern); }
  .photo--before { left: 367px; top: 103px; width: 97px; height: 219px; background: var(--photo-before); }
  .photo--after { left: 467px; top: 103px; width: 154px; height: 219px; background: var(--photo-after); }
  .front-art { z-index: 2; }
</style>
</head>
<body>
<main class="stage">

  <section class="postcard postcard--back" aria-label="Postcard back">
    <svg width="621" height="403" viewBox="0 0 621 403">
      <polygon class="shape-red" points="0,0 186,0 196,18 413,18 413,41 0,41"/>
      <rect class="shape-blue" x="0" y="41" width="413" height="136"/>
      <text class="cta-heading" x="200" y="84" text-anchor="middle">CALL NOW FOR AN ESTIMATE!</text>
      <text class="cta-phone" x="200" y="120" text-anchor="middle">555-318-2764</text>
      <text class="cta-email" x="200" y="158" text-anchor="middle">Dean@wroughtgatestudio.example</text>
    </svg>
  </section>

  <section class="postcard postcard--front" aria-label="Postcard front">
    <div class="photo photo--portrait" role="img" aria-label="Portrait photo of owner Dean Harlowe"></div>
    <div class="photo photo--modern" role="img" aria-label="Modern wooden double door"></div>
    <div class="photo photo--before" role="img" aria-label="Worn wooden double door before replacement"></div>
    <div class="photo photo--after" role="img" aria-label="Ornate iron double door after installation"></div>

    <svg class="front-art" width="621" height="403" viewBox="0 0 621 403">
      <text class="tagline" x="22" y="47" textLength="464" lengthAdjust="spacingAndGlyphs">DESIGN THE SMILE YOUR HOME DESERVES</text>

      <circle class="shape-blue" cx="534" cy="40" r="5"/>
      <text class="brand-name" x="544" y="38">WROUGHT GATE</text>
      <text class="brand-name" x="544" y="48">STUDIO</text>

      <polygon class="shape-red" points="0,63 179,63 186,78 621,78 621,98 196,98 190,83 0,83"/>
      <polygon class="shape-blue" points="0,83 190,83 196,98 621,98 621,103 0,103"/>
      <text class="subline" x="360" y="92" text-anchor="middle">SUPERIOR QUALITY MEETS BEAUTIFUL ELEGANCE</text>

      <polygon fill="#ffffff" points="128,103 209,103 209,322 150,322"/>
      <polygon class="shape-blue" points="98,83 130,83 212,322 150,322"/>
      <polygon class="shape-red" points="128,103 140,103 203,322 190,322"/>
      <polygon class="shape-red" points="143,103 150,103 210,322 203,322"/>

      <rect class="shape-blue" x="209" y="308" width="78" height="14"/>
      <rect class="shape-blue" x="367" y="308" width="60" height="14"/>
      <rect class="shape-blue" x="467" y="308" width="50" height="14"/>
      <text class="photo-label" x="236" y="319">MODERN</text>
      <text class="photo-label" x="371" y="319">BEFORE</text>
      <text class="photo-label" x="471" y="319">AFTER</text>

      <rect class="shape-blue" x="0" y="322" width="150" height="39"/>
      <text class="owner-name" x="20" y="344">DEAN HARLOWE</text>

      <polygon class="shape-blue" points="149,322 621,322 621,403 170,403"/>
      <text class="contact-line" x="181" y="368">555-318-2764  •  Dean@wroughtgatestudio.example</text>
    </svg>
  </section>

</main>
</body>
</html>
```